Hello my company is called Tolvek Coffee.

I want to design a label for the Coffee and Chocolate that we sell in bags.

I want a label that will have:
1. The logo of the attached files, or uplifted version.
2. The "Brisenhart Quell" white circle on the right upper corner of the label.
3. Below the label I will like to have:
Tolvek Coffee
Coffee Antigua Guatemala
250 grams
5. www.tolvekbrew.example (on the left side of the label in vertical position)
6. label shape is rectangular
7. A a separate label for the ingredients with this information:
Coffee Organic
Guatemala
Store in a cool, dry place. Packed in Australia from imported ingredients by Brisenhart Quell Pty Ltd. 17 Wrenfield Crescent Mount Victoria. NSW , Australia.
www.tolvekbrew.example
contains nuts or nuts trace.

thank you
Petronel

Brisenhart Quell

• I want to design a label for the Coffee and Chocolate that we sell in bags.

Tolvek Coffee
Coffee Antigua Guatemala
250 grams
Coffee Organic
Guatemala
www.tolvekbrew.example

thank you
Petronel

```html
<!DOCTYPE html>
<html lang="en">
<head>
<meta charset="utf-8">
<title>Tolvek Coffee Labels</title>
<link rel="stylesheet" href="https://fonts.googleapis.com/css2?family=Yanone+Kaffeesatz:wght@300;400;700&family=Andika&display=swap">
<style>
  :root {
    --bg: #ffffff;
    --label-yellow: #efc118;
    --berry: #d04060;
    --leaf: #6be858;
    --leaf-soft: #8fdc55;
    --forest: #426b50;
    --ink: #111111;
    --olive-ink: #3f5a2c;
    --paper: #ffffff;
  }
  * { margin: 0; padding: 0; box-sizing: border-box; }
  html, body { width: 1200px; height: 932px; overflow: hidden; background: var(--bg); }
  .canvas { position: relative; width: 1200px; height: 932px; }

  .front-label {
    position: absolute; left: 221px; top: 157px; width: 389px; height: 584px;
    background: var(--label-yellow);
  }
  .front-label .frame {
    position: absolute; left: 16px; top: 16px; width: 300px; height: 361px;
    border: 3px solid var(--paper);
  }
  .front-label .artwork {
    position: absolute; left: 84px; top: 31px; width: 220px; height: 335px;
  }
  .front-label .vertical-url {
    position: absolute; left: 54px; top: 198px;
    transform: translate(-50%, -50%) rotate(-90deg);
    font-family: "Andika", sans-serif; font-size: 27px; color: var(--forest);
    white-space: nowrap; letter-spacing: 0.5px;
  }
  .front-label .badge {
    position: absolute; left: 254px; top: 19px; width: 118px; height: 118px;
    border-radius: 50%; background: var(--paper);
    display: flex; align-items: center; justify-content: center; text-align: center;
    font-family: "Yanone Kaffeesatz", sans-serif; font-weight: 700; font-size: 22px;
    line-height: 1.2; color: var(--ink); transform: rotate(5deg);
  }
  .front-label .brand {
    position: absolute; left: 20px; top: 400px;
    font-family: "Yanone Kaffeesatz", sans-serif; font-weight: 700; font-size: 42px; color: var(--ink);
  }
  .front-label .origin {
    position: absolute; left: 20px; top: 450px;
    font-family: "Yanone Kaffeesatz", sans-serif; font-weight: 400; font-size: 31px; color: var(--berry);
  }
  .front-label .weight {
    position: absolute; left: 20px; top: 500px;
    font-family: "Yanone Kaffeesatz", sans-serif; font-weight: 300; font-size: 24px; color: var(--berry);
  }

  .info-label {
    position: absolute; left: 693px; top: 157px; width: 306px; height: 445px;
    background: var(--label-yellow); overflow: hidden;
    font-family: "Yanone Kaffeesatz", sans-serif; color: var(--olive-ink);
  }
  .info-label .product-name {
    position: absolute; left: 14px; top: 16px;
    font-weight: 700; font-size: 43px; color: var(--berry); line-height: 1;
  }
  .info-label .block {
    position: absolute; left: 14px; width: 282px;
    font-size: 21px; line-height: 20px;
  }
  .info-label .ingredients { top: 62px; }
  .info-label .storage { top: 150px; }
  .info-label .packer { top: 176px; }
  .info-label .allergen { top: 262px; font-size: 17px; color: var(--berry); }
  .info-label .more { top: 288px; font-size: 17px; }
  .info-label .site {
    position: absolute; left: 14px; top: 304px;
    font-family: "Andika", sans-serif; font-size: 22px; color: var(--paper); z-index: 2;
    white-space: nowrap;
  }
  .info-label .corner-art {
    position: absolute; left: 132px; top: 301px; width: 170px; height: 144px;
  }
</style>
</head>
<body>
<main class="canvas">
  <section class="front-label">
    <div class="frame"></div>
    <svg class="artwork" viewBox="0 0 220 335" role="img" aria-label="Illustration of terraced coffee hills in green, ochre and berry red under a dark green sky">
      <defs>
        <linearGradient id="hills" x1="0" y1="0" x2="0" y2="1">
          <stop offset="0" stop-color="#426b50"/>
          <stop offset="0.25" stop-color="#6be858"/>
          <stop offset="0.5" stop-color="#e8b23a"/>
          <stop offset="1" stop-color="#d04060"/>
        </linearGradient>
      </defs>
      <rect width="220" height="335" fill="url(#hills)" stroke="#426b50" stroke-width="3"/>
    </svg>
    <div class="vertical-url">www.tolvekbrew.example</div>
    <div class="badge">Brisenhart<br>Quell</div>
    <h1 class="brand">Tolvek Coffee</h1>
    <p class="origin">Antigua Guatemala coffee</p>
    <p class="weight">250 grams</p>
  </section>

  <section class="info-label">
    <h2 class="product-name">Cacao Brasa</h2>
    <p class="block ingredients">Ingredients:<br>Sesame seeds, Chili, Cinnamon, Sugar, Cacao Butter, Cacao Liquor, Emulsifiers, Soy Lecithin 476, Cocoa solids 48%</p>
    <p class="block storage">Store in a cool, dry place.</p>
    <p class="block packer">Packed in Australia from imported ingredients by Brisenhart Quell Pty Ltd.<br>17 Wrenfield Crescent Dunmere Hollow.<br>WR 3090, Australia.</p>
    <p class="block allergen">May contain nuts or nuts trace</p>
    <p class="block more">For more Coffee and Chocolates flavors please visit</p>
    <div class="site">www.tolvekbrew.example</div>
    <svg class="corner-art" viewBox="0 0 170 144" role="img" aria-label="Corner illustration of terraced berry-red and green coffee hills">
      <defs>
        <linearGradient id="corner" x1="0" y1="1" x2="1" y2="0">
          <stop offset="0" stop-color="#6be858"/>
          <stop offset="0.5" stop-color="#d04060"/>
          <stop offset="1" stop-color="#8fdc55"/>
        </linearGradient>
      </defs>
      <path d="M0 144 Q60 40 170 0 L170 144 Z" fill="url(#corner)"/>
    </svg>
  </section>
</main>
</body>
</html>
```